Property developer, money partner needs business card design using logo concept provided

Our company develops residential properties, does money lends for joint ventures in property deals and finds property deals for other money partners. We have provided a basic logo for you to work from. Any graphic or logo design on the card is to communicate development and finance collaboration. Color choice is not so important for us, but color choice does need to reflect professionalism.

```html
<!DOCTYPE html>
<html lang="en">
<head>
<meta charset="utf-8">
<title>Brightlot Property Solutions – Business Card</title>
<link rel="stylesheet" href="https://fonts.googleapis.com/css2?family=Exo+2:wght@800&family=Montserrat:wght@500;800&family=Lato:wght@400&display=swap">
<style>
  :root {
    --stage: #e9ebee;
    --blue-light: #0a72c2;
    --blue-deep: #053d8e;
    --blue-name: #0b5fb3;
    --ink: #1d1d1f;
    --accent-red: #b3121b;
    --paper: #ffffff;
  }
  html, body {
    margin: 0;
    width: 1200px;
    height: 939px;
    overflow: hidden;
    background: var(--stage);
  }
  .canvas {
    position: relative;
    width: 1200px;
    height: 939px;
  }
  .card {
    position: absolute;
    width: 525px;
    height: 300px;
    box-shadow: 0 8px 24px rgba(0,0,0,0.18);
    box-sizing: border-box;
  }
  /* Front */
  .card-front {
    left: 60px;
    top: 150px;
    background: linear-gradient(135deg, var(--blue-light) 0%, var(--blue-deep) 100%);
    display: flex;
    flex-direction: column;
    align-items: center;
    justify-content: center;
    color: var(--paper);
    font-family: "Montserrat", sans-serif;
  }
  .brand-dot {
    width: 96px;
    height: 96px;
    border-radius: 50%;
    background: var(--paper);
    margin-bottom: 22px;
  }
  .brand-name {
    font-weight: 800;
    font-size: 30px;
    letter-spacing: 6px;
    line-height: 1;
  }
  .brand-sub {
    font-weight: 500;
    font-size: 15px;
    letter-spacing: 3px;
    margin-top: 6px;
  }
  .brand-acn {
    font-weight: 500;
    font-size: 9px;
    letter-spacing: 2px;
    margin-top: 3px;
  }
  /* Back */
  .card-back {
    left: 615px;
    top: 490px;
    background: var(--paper);
    font-family: "Lato", sans-serif;
    color: var(--ink);
  }
  .person {
    position: absolute;
    left: 38px;
    top: 62px;
  }
  .person-name {
    font-family: "Exo 2", sans-serif;
    font-weight: 800;
    font-size: 27px;
    letter-spacing: 1px;
    color: var(--blue-name);
    margin: 0;
    line-height: 1;
  }
  .person-role {
    font-size: 13px;
    margin-top: 4px;
  }
  .address {
    position: absolute;
    left: 58px;
    top: 140px;
    font-size: 13px;
    line-height: 1.45;
    font-style: normal;
  }
  .contact-list {
    position: absolute;
    left: 58px;
    top: 196px;
    margin: 0;
    padding: 0;
    list-style: none;
    font-size: 13px;
    line-height: 1.55;
  }
  .contact-list li {
    display: flex;
    align-items: center;
    gap: 7px;
  }
  .contact-list svg {
    width: 11px;
    height: 11px;
    fill: var(--accent-red);
    flex: none;
  }
  .back-brand {
    position: absolute;
    right: 34px;
    top: 44px;
    display: flex;
    flex-direction: column;
    align-items: center;
    color: var(--ink);
    font-family: "Montserrat", sans-serif;
  }
  .back-brand .brand-dot {
    width: 78px;
    height: 78px;
    background: var(--blue-name);
    margin-bottom: 16px;
  }
  .back-brand .brand-name { font-size: 22px; letter-spacing: 4px; }
  .back-brand .brand-sub { font-size: 11px; letter-spacing: 2px; margin-top: 4px; }
  .back-brand .brand-acn { font-size: 7px; }
</style>
</head>
<body>
<main class="canvas">
  <section class="card card-front" aria-label="Card front">
    <div class="brand-dot"></div>
    <div class="brand-name">BRIGHTLOT</div>
    <div class="brand-sub">Property Solutions</div>
    <div class="brand-acn">A.C.N 418 203 961</div>
  </section>

  <section class="card card-back" aria-label="Card back">
    <div class="person">
      <h1 class="person-name">DANIEL REEVE</h1>
      <div class="person-role">Owner/Director</div>
    </div>
    <address class="address">4/17 Ferntree Ave,<br>Ringwood VIC 3134</address>
    <ul class="contact-list">
      <li>
        <svg viewBox="0 0 24 24" aria-hidden="true"><path d="M6.6 10.8a15.1 15.1 0 0 0 6.6 6.6l2.2-2.2a1 1 0 0 1 1-.25 11.4 11.4 0 0 0 3.6.57 1 1 0 0 1 1 1V20a1 1 0 0 1-1 1A17 17 0 0 1 3 4a1 1 0 0 1 1-1h3.5a1 1 0 0 1 1 1c0 1.25.2 2.45.57 3.57a1 1 0 0 1-.25 1z"/></svg>
        0412 555 019
      </li>
      <li>
        <svg viewBox="0 0 24 24" aria-hidden="true"><path d="M2 5h20v14H2z M2 5l10 8 10-8" /></svg>
        hello@brightlotproperty.com.au
      </li>
      <li>
        <svg viewBox="0 0 24 24" aria-hidden="true"><circle cx="12" cy="12" r="10"/></svg>
        brightlotproperty.com.au
      </li>
    </ul>
    <div class="back-brand">
      <div class="brand-dot"></div>
      <div class="brand-name">BRIGHTLOT</div>
      <div class="brand-sub">Property Solutions</div>
      <div class="brand-acn">A.C.N 418 203 961</div>
    </div>
  </section>
</main>
</body>
</html>
```